Business card for Autism Consultancy

I need a double-sided business card for Brightpath Learning Consultancy
Please try to use the colours and graphics in line with our website www.brightpathlearn.nz
Front side
Logo and the name of the company – Brightpath Learning Consultancy
We use Child-Centred, Modern and Innovative approaches
Teaching autistic children to bond, laugh and play
www.brightpathlearn.nz
info@brightpathlearn.nz
phone +64 09 37 615 48
Back side
Photo
Mirela Dunstan
Founder
Postgraduate Autism (Children) Specialist (with Merit)
Qualified by the Faculty of Learning Support and Access Studies (FLSA), Harwell Vale University
mirela@brightpathlearn.nz
phone +64 937 615 48
mobile: +64 20 6283 9150
Please do not convert the text fields to outlines, i.e. I need to be able to edit any text after.
The final design should be either in Adobe Illustrator or Adobe Photoshop format.
The Specs for the business card are:
Full Bleed Size
94 x 58 mm
1110 x 685 pixels
Document Trim Size
91 x 55 mm
1075 x 650 pixels

```html
<!DOCTYPE html>
<html lang="en">
<head>
<meta charset="utf-8">
<title>Mirela Dunstan – Business Card Back</title>
<link rel="stylesheet" href="https://fonts.googleapis.com/css2?family=Nunito+Sans:wght@600;700&display=swap">
<style>
  :root {
    --card-green: #48ee9b;
    --white: #ffffff;
    --portrait-light: #fbf8f5;
    --portrait-warm: #e9ddd3;
  }
  html, body {
    margin: 0;
    padding: 0;
    width: 1200px;
    height: 741px;
    overflow: hidden;
    background: var(--card-green);
  }
  .card {
    position: relative;
    width: 1200px;
    height: 741px;
    background: var(--card-green);
    font-family: "Nunito Sans", sans-serif;
    color: var(--white);
  }
  .portrait {
    position: absolute;
    left: 68px;
    top: 74px;
    width: 594px;
    height: 594px;
  }
  .details {
    position: absolute;
    right: 57px;
    top: 0;
    width: 640px;
    text-align: right;
  }
  .name {
    position: absolute;
    right: 10px;
    top: 117px;
    margin: 0;
    font-size: 56px;
    font-weight: 600;
    letter-spacing: 0.5px;
    white-space: nowrap;
  }
  .role {
    position: absolute;
    right: 0;
    top: 213px;
    margin: 0;
    font-size: 28px;
    font-weight: 700;
  }
  .credentials {
    position: absolute;
    right: 0;
    top: 275px;
    margin: 0;
    font-size: 21.5px;
    line-height: 32px;
    font-weight: 700;
    white-space: nowrap;
  }
  .contact {
    position: absolute;
    right: 0;
    top: 480px;
    margin: 0;
    padding: 0;
    list-style: none;
    font-size: 31px;
    font-weight: 700;
    line-height: 60px;
    letter-spacing: 0.3px;
    white-space: nowrap;
  }
</style>
</head>
<body>
  <main class="card">
    <svg class="portrait" viewBox="0 0 594 594" role="img" aria-label="Portrait photo of Mirela Dunstan, founder">
      <defs>
        <radialGradient id="portraitTone" cx="50%" cy="50%" r="50%">
          <stop offset="0%" stop-color="var(--portrait-warm)"/>
          <stop offset="100%" stop-color="var(--portrait-light)"/>
        </radialGradient>
      </defs>
      <circle cx="297" cy="297" r="297" fill="url(#portraitTone)"/>
    </svg>

    <section class="details">
      <h1 class="name">Mirela Dunstan</h1>
      <p class="role">Founder</p>
      <p class="credentials">
        Postgraduate Autism (Children)<br>
        Specialist (with Merit) Qualified<br>
        by the Faculty of Learning Support<br>
        and Access Studies (FLSA)<br>
        Harwell Vale University
      </p>
      <ul class="contact">
        <li class="contact-phone">phone +64 937 615 48</li>
        <li class="contact-mobile">mobile: +64 20 6283 9150</li>
        <li class="contact-email">mirela@brightpathlearn.nz</li>
      </ul>
    </section>
  </main>
</body>
</html>
```